Website for Kitchen Showroom

We need a website for our Kitchen Showroom. Will be 10 pages in total. Example of a website we like can be found at http://www.brivantaform.co.uk/ with the image on the front page being a java script slideshow picking up images from a directory that I can update. Looking for simple SEO
I have the wording/ sitemap/ images all ready to go and I am looking for a quick turn around.
Thank you for your time. Tom

```html
<!DOCTYPE html>
<html lang="en">
<head>
<meta charset="utf-8">
<title>Hearth &amp; Grain – Kitchen Showroom</title>
<link href="https://fonts.googleapis.com/css2?family=Didact+Gothic&family=PT+Sans:wght@400;700&display=swap" rel="stylesheet">
<style>
:root{
  --green:#7dc21e;
  --green-dark:#5a9a0c;
  --green-light:#a6e23a;
  --ink:#333;
  --logo-grey:#6e6e6e;
  --footer-text:#d6d6d6;
  --white:#fff;
}
*{margin:0;padding:0;box-sizing:border-box}
html,body{width:1022px;height:1200px;overflow:hidden;background:var(--white)}
body{position:relative;font-family:"PT Sans",sans-serif;color:var(--ink)}
.abs{position:absolute}

.top-rule{left:0;top:0;width:1022px;height:3px;background:var(--green)}
.header{left:0;top:3px;width:1022px;height:117px;background:linear-gradient(#fff,#ececec)}
.brand{left:82px;top:24px;display:flex;align-items:center;gap:14px}
.brand-mark{width:70px;height:70px;background:var(--green)}
.brand-name{font-family:"Didact Gothic",sans-serif;font-size:39px;line-height:38px;color:var(--logo-grey)}

.search{left:684px;top:0;width:262px;height:37px;background:linear-gradient(var(--green-light),var(--green-dark));border-radius:0 0 12px 12px}
.search-field{left:18px;top:8px;width:190px;height:20px;background:#fff;border:1px solid #ccc;font-size:9px;color:#888;padding:4px 3px}
.search-btn{left:222px;top:5px;width:27px;height:27px;border-radius:50%;background:radial-gradient(circle at 40% 35%,#d9f59e,var(--green-dark))}

.shop{left:787px;top:64px;width:154px;height:46px;border:1px solid #ddd;border-radius:10px;background:#fafafa;text-align:right;padding:3px 9px 0 0}
.shop-line1{font-size:14px;line-height:19px;color:#999}
.shop-line2{font-size:14px;line-height:19px;color:var(--green);letter-spacing:.5px}
.shop-icon{left:-8px;top:-12px}

.nav{left:0;top:120px;width:1022px;height:32px;background:linear-gradient(#3d3d3d,#1e1e1e)}
.nav ul{list-style:none;display:flex;align-items:center;justify-content:space-between;height:32px;margin-left:69px;width:871px}
.nav li{font-size:10px;color:#fff;letter-spacing:.2px}
.nav li.sep{color:#ccc}
.nav li.active{background:var(--green);height:29px;line-height:29px;padding:0 10px}

.hero{left:0;top:152px;width:1022px;height:354px;background:linear-gradient(180deg,#e4e4e4,#c8d49a)}
.hero-base{left:0;top:506px;width:1022px;height:21px;background:linear-gradient(#f4f4f4,#e2e2e2)}

.rule{height:1px;background:linear-gradient(90deg,transparent,#d9d9d9 20%,#d9d9d9 80%,transparent)}
.intro-bg{left:70px;top:545px;width:915px;height:138px;background:linear-gradient(90deg,#fff,#f3f3f3 60%,#fff)}
.intro-photo{left:92px;top:556px;width:118px;height:118px;border-radius:50%;border:7px solid var(--green-light);background:linear-gradient(#6aa7cf,#4d7e9f)}
.intro-text{left:221px;top:562px;width:708px;font-size:11px;line-height:17.8px;color:#444;text-align:justify}
.intro-text p+p{margin-top:17.8px}

.card{top:710px;width:200px}
.card h2{font-family:"Didact Gothic",sans-serif;font-weight:400;font-size:20px;color:#666;margin:0 0 10px 3px}
.card .photo{width:198px;height:110px;border:5px solid #cfcfcf}
.card p{font-size:10px;line-height:17.8px;color:#333;text-align:justify;width:191px;margin:12px 0 0 4px}
.more{top:987px;width:64px;height:15px;border-radius:8px;background:linear-gradient(var(--green-light),var(--green-dark));color:#fff;font-size:9.5px;text-align:center;line-height:15px}

.footer{left:0;top:1023px;width:1022px;height:177px;background:linear-gradient(#474747,#2a2a2a)}
.f-col{top:1030px}
.f-col h3{font-family:"Didact Gothic",sans-serif;font-weight:400;font-variant:small-caps;font-size:19px;color:#ccc}
.f-col ul{list-style:none;margin-top:12px}
.f-col li{font-size:10px;color:var(--footer-text);line-height:17.8px;padding-left:16px;position:relative}
.f-col li::before{content:"";position:absolute;left:0;top:6px;width:5px;height:5px;border-radius:50%;background:var(--green)}
.news{font-size:10px;color:var(--footer-text);line-height:12px}
.copy{left:75px;top:1174px;font-size:11.5px;color:#ddd}
.legal{left:666px;top:1179px;font-size:11px;color:#ddd;word-spacing:2px}
</style>
</head>
<body>
<div class="abs header"></div>
<div class="abs top-rule"></div>

<div class="abs brand">
  <div class="brand-mark"></div>
  <div class="brand-name">hearth<br>&amp; grain</div>
</div>

<div class="abs search">
  <div class="abs search-field">-------search products-----------</div>
  <div class="abs search-btn"></div>
</div>

<div class="abs shop">
  <svg class="abs shop-icon" width="30" height="30" viewBox="0 0 30 30">
    <path d="M4 6h4l3 12h12l3-9H10" fill="none" stroke="#4a7fc1" stroke-width="1.6"/>
    <circle cx="12" cy="22" r="1.8" fill="#555"/><circle cx="21" cy="22" r="1.8" fill="#555"/>
    <circle cx="6" cy="20" r="5" fill="var(--green)"/>
    <path d="M6 17v6M3 20h6" stroke="#fff" stroke-width="1.6"/>
  </svg>
  <div class="shop-line1">Click here to visit</div>
  <div class="shop-line2">ON LINE SHOPPING</div>
</div>

<nav class="abs nav">
  <ul>
    <li class="active">HOME</li><li class="sep">|</li>
    <li>ABOUT US</li><li class="sep">|</li>
    <li>COLOURS</li><li class="sep">|</li>
    <li>APPLICATIONS</li><li class="sep">|</li>
    <li>PRODUCTS</li><li class="sep">|</li>
    <li>NEWS</li><li class="sep">|</li>
    <li>GALLERY</li><li class="sep">|</li>
    <li>WHERE TO VIEW</li><li class="sep">|</li>
    <li>FAQ</li><li class="sep">|</li>
    <li>CONTACT US</li><li class="sep">|</li>
    <li>SHOPE ONLINE</li>
  </ul>
</nav>

<div class="abs hero" role="img" aria-label="Showroom photo of a modern kitchen in lime green and grey"></div>
<div class="abs hero-base"></div>

<div class="abs intro-bg"></div>
<div class="abs rule" style="left:80px;top:544px;width:860px"></div>
<div class="abs rule" style="left:70px;top:683px;width:920px"></div>
<div class="abs intro-photo" role="img" aria-label="Colourful kitchenware"></div>
<div class="abs intro-text">
  <p>Lorem Ipsum is simply dummy text of the printing and typesetting industry. Lorem Ipsum has been the industry's standard dummy text ever since the 1500s, when an unknown printer took a galley of type and scrambled it to make a type specimen book. It has survived not only five centuries, but also the leap into electronic typesetting,</p>
  <p>remaining essentially unchanged. It was popularised in the 1960s with the release of Typeset Co sheets containing Lorem Ipsum passages, and more recently with desktop publishing software like PageCraft including versions of Lorem Ipsum.</p>
</div>

<section class="abs card" style="left:76px">
  <h2>Request a brochure</h2>
  <div class="photo" style="background:linear-gradient(#8c7c70,#a89a8e)" role="img" aria-label="Kitchen photo in warm brown and cream tones"></div>
  <p>Lorem Ipsum is simply dummy text of the printing and typesetting industry. Lorem Ipsum has been the industry's standard dummy text ever since the 1500s, when an unknown printer took a galley of type and scrambled it.</p>
</section>
<section class="abs card" style="left:303px">
  <h2>Designer 3d</h2>
  <div class="photo" style="background:linear-gradient(#dcdcdc,#c2bcb6)" role="img" aria-label="Bright open-plan kitchen photo"></div>
  <p>Lorem Ipsum is simply dummy text of the printing and typesetting industry. Lorem Ipsum has been the industry's standard dummy text ever since the 1500s, when an unknown printer took a galley of type and scrambled it.</p>
</section>
<section class="abs card" style="left:529px">
  <h2>New Design</h2>
  <div class="photo" style="background:linear-gradient(#6a5e56,#4e433d)" role="img" aria-label="Dark wood kitchen photo"></div>
  <p>Lorem Ipsum is simply dummy text of the printing and typesetting industry. Lorem Ipsum has been the industry's standard dummy text ever since the 1500s, when an unknown printer took a galley of type and scrambled it.</p>
</section>
<section class="abs card" style="left:755px">
  <h2>Design Palette</h2>
  <div class="photo" style="background:linear-gradient(#c8701c,#a95a14)" role="img" aria-label="Warm orange kitchen photo"></div>
  <p>Lorem Ipsum is simply dummy text of the printing and typesetting industry. Lorem Ipsum has been the industry's standard dummy text ever since the 1500s, when an unknown printer took a galley of type and scrambled it.</p>
</section>

<div class="abs more" style="left:203px">More info..</div>
<div class="abs more" style="left:427px;top:986px">More info..</div>
<div class="abs more" style="left:660px">More info..</div>
<div class="abs more" style="left:888px">More info..</div>

<footer class="abs footer"></footer>
<div class="abs f-col" style="left:97px">
  <h3 style="margin-left:16px">About us</h3>
  <ul><li>Quarrystone Australia</li><li>Environmental Commitment</li><li>Careers &amp; Opportunities</li><li>Office Locations</li></ul>
</div>
<div class="abs f-col" style="left:279px">
  <h3>Applications</h3>
  <ul><li>Kitchen</li><li>Bathroom</li><li>Commercial</li><li>Furniture</li></ul>
</div>
<div class="abs f-col" style="left:433px">
  <h3 style="margin-left:11px">Products</h3>
  <ul><li>Quarrystone Vero</li><li>Quarrystone Linea</li><li>Quarrystone Alto</li><li>Quarrystone Forma</li></ul>
</div>
<div class="abs f-col" style="left:608px">
  <h3 style="margin-left:8px">Gallery</h3>
  <ul style="margin-top:5px"><li>Residential Gallery</li><li>Commercial Gallery</li><li>Projects</li></ul>
</div>
<div class="abs f-col" style="left:783px">
  <h3>Latest news</h3>
  <div class="news" style="margin-top:8px">07.02.11 &nbsp; VISTAGLASS</div>
  <div class="news" style="margin-top:13px">Our newest product Vistaglass high<br>&nbsp;resolution images printed<br>&nbsp;onto glass is…</div>
</div>

<div class="abs copy">Copyright © Hearth &amp; Grain 2010 - 2011. All Rights Reserved.</div>
<div class="abs legal">Terms &amp; Conditions &nbsp; | &nbsp; Terms of Use &nbsp; | &nbsp; Privacy policy</div>
</body>
</html>
```